Website Design for PawRank - New Digital Agency

We are creating a new digital marketing agency and need a new website. I have attached the logo. Our niche is going to be veterinarians. Use the same colors as in the logo (blue, white and gray).

I want real pictures of real people in this and not just boring stock photos. It needs to be related to the industry.

Home page (example:https://linkvorta.com/)
Service page (example: https://darvimosk.com/consulting/)
Case study page (example: https://www.tomaswellbry.com/seo/case-study/)

I will continue to update this brief.
Updates

I updated the brief with some additional sample sites 2 days ago and want to see more designs. I won't need that may more days ...just a few more.

Target Market(s)

veterinarians

Font styles to use
Sans Serif

Requirements
Must have
• I want a very clean looking site. Use the same colors as in the logo (blue, white and gray).
Nice to have
• We need to build this with the idea that the purpose is to generate leads for our business.
• Home page (example:https://linkvorta.com/)
• Service page (example: https://darvimosk.com/consulting/)
• Case study page (example: https://www.tomaswellbry.com/seo/case-study/)

```html
<!DOCTYPE html>
<html lang="en">
<head>
<meta charset="utf-8">
<title>PawRank – Digital Marketing Agency</title>
<link href="https://fonts.googleapis.com/css2?family=Rubik:wght@500;700;800&family=Lato:ital,wght@0,400;0,700;1,400&family=Montserrat:wght@500;600&display=swap" rel="stylesheet">
<style>
:root{
  --blue:#0f53a8;
  --blue-bright:#1d6fd0;
  --blue-band:#2b63ae;
  --blue-pale:#e5edf6;
  --ink:#222;
  --grey:#8a8a8a;
  --dark:#2b2b2b;
  --white:#fff;
}
*{margin:0;padding:0;box-sizing:border-box}
html,body{width:1200px;height:3859px;overflow:hidden;background:var(--white)}
body{position:relative;font-family:'Lato',sans-serif;color:var(--ink)}
.abs{position:absolute}
.heading{font-family:'Rubik',sans-serif;font-weight:700;font-size:44px;color:var(--ink);text-align:center;width:1200px;left:0}
.rule{position:absolute;height:2px;width:125px;background:var(--blue)}
.btn{position:absolute;display:flex;align-items:center;justify-content:center;background:var(--blue);color:var(--white);font-family:'Lato',sans-serif;font-weight:700;font-size:16px;text-transform:uppercase;border-radius:0 22px 22px 22px;text-decoration:none}

/* header + hero */
.hero-art{position:absolute;left:0;top:0}
.brand{left:77px;top:30px;display:flex;align-items:center;gap:10px;font-family:'Lato',sans-serif;font-weight:700;font-size:40px;color:var(--white)}
.brand-dot{width:28px;height:28px;border-radius:50%;background:var(--blue-bright)}
.nav{left:424px;top:46px;display:flex;gap:0;font-size:15px;color:#ddd}
.nav a{color:#ddd;text-decoration:none;position:absolute;white-space:nowrap}
.nav a.active{color:var(--white);font-weight:700}
.nav-bar{position:absolute;left:420px;top:101px;width:50px;height:3px;background:var(--blue-bright)}
.header-line{position:absolute;left:0;top:104px;width:1200px;height:1px;background:rgba(255,255,255,.25)}
.quote-btn{left:967px;top:21px;width:156px;height:62px;font-size:15px}
.hero-title{top:270px;width:1200px;text-align:center;font-family:'Rubik',sans-serif;font-weight:800;font-size:86px;color:var(--blue-bright);letter-spacing:1px}
.hero-sub{top:380px;width:1200px;text-align:center;font-family:'Montserrat',sans-serif;font-weight:600;font-size:48px;line-height:52px;color:var(--white)}

/* about */
.about-title{left:78px;top:752px;font-family:'Rubik',sans-serif;font-weight:700;font-size:42px}
.about-text{left:508px;top:756px;width:600px;font-size:16px;line-height:31.5px;color:var(--grey)}
.about-text p+p{margin-top:20px}

/* services */
.services-band{position:absolute;left:0;top:1197px;width:1200px;height:553px;background:var(--blue-pale);border-top-left-radius:300px 210px}
.service-card{position:absolute;top:1396px;width:313px;height:270px;background:var(--white);border-radius:0 0 46px 0;display:flex;flex-direction:column;align-items:center;padding-top:40px}
.service-card svg{width:110px;height:110px}
.service-card h3{margin-top:22px;font-family:'Montserrat',sans-serif;font-weight:500;font-size:21px;line-height:26px;text-align:center;color:var(--ink)}

/* why */
.why-band{position:absolute;left:0;top:1750px;width:1200px;height:563px;background:linear-gradient(120deg,#2f69b4,#2a5fa8 50%,#3a74bc)}
.why-frame{left:77px;top:2063px;width:1046px;height:166px;border:2px dashed rgba(255,255,255,.55)}
.why-card{position:absolute;top:1969px;width:188px;height:187px;background:var(--white);display:flex;flex-direction:column;align-items:center;padding-top:24px}
.why-card svg{width:76px;height:76px}
.why-card p{margin-top:14px;font-family:'Montserrat',sans-serif;font-weight:500;font-size:16px;line-height:26px;text-align:center;color:#555}
.why-dot{left:580px;top:2209px;width:40px;height:40px;border-radius:50%;background:rgba(255,255,255,.85)}

/* feedback */
.feedback-card{left:288px;top:2573px;width:624px;height:292px;background:var(--white);border-radius:6px;box-shadow:0 4px 24px rgba(0,0,0,.08)}
.avatar{left:548px;top:2520px;width:104px;height:104px;border-radius:50%;background:linear-gradient(160deg,#c9d3de,#7d8893);border:3px solid var(--white)}
.client-name{top:2644px;width:1200px;text-align:center;color:var(--blue-bright);font-weight:700;font-size:15px}
.client-role{top:2671px;width:1200px;text-align:center;color:var(--grey);font-size:13px}
.client-quote{left:360px;top:2715px;width:480px;text-align:center;color:var(--grey);font-size:14px;line-height:27px}
.qmark{font-family:'Rubik',sans-serif;font-weight:800;font-size:64px;color:var(--blue-bright);line-height:1}
.dots{top:2917px;left:500px;display:flex;gap:20px}
.dots span{width:53px;height:3px;background:#cfcfcf;border-radius:2px}
.dots span.on{background:var(--blue);height:4px}

/* cta + footer */
.cta-title{top:3105px;font-family:'Rubik',sans-serif;font-weight:700;font-size:44px;line-height:53px;color:var(--white);text-align:center;width:1200px}
.footer-title{top:3457px;font-family:'Rubik',sans-serif;font-weight:700;font-size:21px;color:var(--white)}
.footer-text{color:var(--white);font-size:14px;line-height:25px}
.contact-row{position:absolute;left:78px;display:flex;gap:16px;align-items:flex-start}
.contact-row svg{width:22px;height:22px;flex:none;margin-top:2px}
.foot-nav{left:348px;top:3511px;list-style:none}
.foot-nav li{display:flex;align-items:center;gap:18px;height:29px;font-size:14px;color:var(--white)}
.foot-nav li::before{content:"";width:7px;height:7px;border:1px solid var(--white)}
.foot-nav li.current{font-weight:700}
.foot-nav li.current::before{background:var(--white)}
.post{position:absolute;left:572px;display:flex;gap:20px}
.post-thumb{width:80px;height:80px;border-radius:50%;border:3px solid var(--white);flex:none}
.post small{display:block;font-style:italic;font-size:13px}
.email-field{left:884px;top:3574px;width:239px;height:62px;background:var(--white);border-radius:4px;display:flex;align-items:center;gap:14px;padding-left:14px;color:#666;font-size:14px}
.subscribe{left:884px;top:3650px;width:187px;height:62px;background:#1c1c1c;font-size:16px}
.footer-line{left:0;top:3773px;width:1200px;height:1px;background:rgba(255,255,255,.25)}
.copyright{top:3806px;width:1200px;text-align:center;color:var(--white);font-size:13px}
</style>
</head>
<body>

<!-- hero -->
<svg class="hero-art" width="1200" height="700" viewBox="0 0 1200 700">
  <path d="M0 0H1200V410C1190 560 1080 680 900 692H0Z" fill="#dbe6f2"/>
  <path d="M0 0H1200V380C1185 540 1080 668 900 678H0Z" fill="#2b2b2b" role="img" aria-label="Photo of a hand gently holding a small pet"/>
  <ellipse cx="470" cy="330" rx="270" ry="190" fill="#3a2f29" opacity=".55"/>
</svg>
<div class="abs brand"><span>PawRank</span><span class="brand-dot"></span></div>
<nav class="abs nav">
  <a class="active" style="left:0">Home</a>
  <a style="left:83px">About</a>
  <a style="left:166px">Services</a>
  <a style="left:260px">Testimonial</a>
  <a style="left:376px">Blog</a>
  <a style="left:442px">Contact</a>
</nav>
<div class="nav-bar"></div>
<div class="header-line"></div>
<a class="btn quote-btn">Get a quote</a>
<h1 class="abs hero-title">PAW RANK</h1>
<p class="abs hero-sub">DIGITAL MARKETING<br>AGENCY</p>

<!-- about -->
<h2 class="abs about-title">About PawRank</h2>
<div class="rule" style="left:78px;top:832px"></div>
<div class="abs about-text">
  <p>Lorem ipsum dolor sit amet, consectetur adipiscing elit, sed do eiusmod tempor incididunt ut labore et dolore magna aliqua. Ut enim minim veniam, quis nostrud exercitation ullamco laboris nisi ut aliquip ex ea commodo consequat. Duis aute irure dolor in reprehenderit in voluptate velit esse cillum.</p>
  <p>Lorem ipsum dolor sit amet, consectetur adipiscing elit, sed do eiusmod tempor incididunt ut labore et dolore magna aliqua. Ut enim minim veniam, quis nostrud exercitation ullamco laboris nisi ut aliquip ex ea commodo consequat. Duis aute irure dolor in reprehenderit in voluptate velit esse cillum.</p>
</div>
<a class="btn" style="left:507px;top:1052px;width:187px;height:62px">Find out more</a>

<!-- services -->
<div class="services-band"></div>
<h2 class="abs heading" style="top:1262px">Provide Services</h2>
<div class="rule" style="left:537px;top:1342px"></div>
<div class="service-card" style="left:77px">
  <svg viewBox="0 0 110 110" fill="none" stroke="#1d6fd0" stroke-width="3"><circle cx="55" cy="55" r="26"/><circle cx="55" cy="55" r="16" fill="#dbe6f2"/><path d="M15 15L95 95M95 15L15 95"/><text x="49" y="62" font-size="20" fill="#0f53a8" stroke="none" font-family="Lato" font-weight="700">$</text></svg>
  <h3>Paid Media</h3>
</div>
<div class="service-card" style="left:443px">
  <svg viewBox="0 0 110 110" fill="none" stroke="#1d6fd0" stroke-width="3"><rect x="30" y="14" width="50" height="84"/><path d="M80 14l14 14v70H80"/><path d="M40 40h30M40 52h30M40 64h16"/><rect x="60" y="68" width="16" height="16"/><path d="M60 68l16 16M76 68l-16 16"/><circle cx="26" cy="20" r="9" fill="#dbe6f2"/></svg>
  <h3>Content Marketing<br>Management</h3>
</div>
<div class="service-card" style="left:810px">
  <svg viewBox="0 0 110 110" fill="none" stroke="#1d6fd0" stroke-width="3"><path d="M18 52l50-30v56l-50-14z" fill="#dbe6f2"/><ellipse cx="70" cy="50" rx="8" ry="28"/><path d="M28 66l8 26M14 98h82M86 30l10-8M88 50h12M86 70l10 8"/></svg>
  <h3>Digital Services</h3>
</div>

<!-- why -->
<div class="why-band" role="img" aria-label="Blue-tinted photo of a vet caring for a pet"></div>
<h2 class="abs heading" style="top:1805px;color:#fff">Why PawRank</h2>
<div class="rule" style="left:537px;top:1895px;background:#fff"></div>
<div class="abs why-frame"></div>
<div class="why-card" style="left:110px">
  <svg viewBox="0 0 76 76" fill="none" stroke="#1d6fd0" stroke-width="2.5"><rect x="14" y="6" width="30" height="60" rx="3"/><path d="M20 22h18M20 32h18M20 42h10M44 34h10l8-6v20l-8-6H44"/></svg>
  <p>Relevant,<br>Powerful Links</p>
</div>
<div class="why-card" style="left:308px">
  <svg viewBox="0 0 76 76" fill="none" stroke="#1d6fd0" stroke-width="2.5"><rect x="10" y="22" width="56" height="44" rx="3"/><path d="M28 22v-8h20v8"/><circle cx="28" cy="44" r="10"/><circle cx="50" cy="48" r="8"/></svg>
  <p>Reduce<br>Operational Costs</p>
</div>
<div class="why-card" style="left:506px">
  <svg viewBox="0 0 76 76" fill="none" stroke="#1d6fd0" stroke-width="2.5"><path d="M18 24h40M24 24l4-16h20l4 16"/><path d="M26 30c0 10 6 16 12 16s12-6 12-16"/><path d="M10 70c0-14 12-22 28-22s28 8 28 22z"/></svg>
  <p>Only White Hat<br>Strategies</p>
</div>
<div class="why-card" style="left:704px">
  <svg viewBox="0 0 76 76" fill="none" stroke="#1d6fd0" stroke-width="2.5"><path d="M16 36a22 22 0 0144 0"/><rect x="10" y="34" width="10" height="16" rx="3"/><rect x="56" y="34" width="10" height="16" rx="3"/><circle cx="38" cy="40" r="14"/><path d="M16 70c2-10 10-14 22-14s20 4 22 14M60 50c0 8-8 10-16 10"/></svg>
  <p>World-class<br>Customer Support</p>
</div>
<div class="why-card" style="left:902px">
  <svg viewBox="0 0 76 76" fill="none" stroke="#1d6fd0" stroke-width="2.5"><circle cx="28" cy="28" r="18"/><circle cx="48" cy="48" r="18"/><path d="M20 32c4 5 12 5 16 0M42 56c3-4 9-4 12 0"/></svg>
  <p>100%<br>Satisfaction</p>
</div>
<div class="abs why-dot"></div>

<!-- feedback -->
<h2 class="abs heading" style="top:2390px">Clients Feedback</h2>
<div class="rule" style="left:537px;top:2469px"></div>
<div class="abs feedback-card"></div>
<div class="abs avatar" role="img" aria-label="Portrait photo of the client"></div>
<p class="abs client-name">-A. DORVELLE</p>
<p class="abs client-role">Manager</p>
<span class="abs qmark" style="left:322px;top:2702px">&ldquo;</span>
<p class="abs client-quote">Lorem ipsum dolor sit amet, consectetur adipiscing elit, sed do eiusmod tempor incididunt ut labore et dolore magna aliqua. Ut enim ad minim veniam, quis nostrud exercitation ullamco laboris nisi ut aliquip ex ea commodo consequat.</p>
<span class="abs qmark" style="left:840px;top:2775px;color:#6b9ad6">&rdquo;</span>
<div class="abs dots"><span></span><span class="on"></span><span></span></div>

<!-- cta + footer shape -->
<svg class="abs" style="left:0;top:3012px" width="1200" height="847" viewBox="0 0 1200 847">
  <rect width="1200" height="400" fill="#6f7f93" role="img" aria-label="Photo of hands holding a puppy"/>
  <rect width="1200" height="400" fill="url(#ctaShade)"/>
  <defs><linearGradient id="ctaShade" x1="0" x2="1"><stop offset="0" stop-color="#9a8680" stop-opacity=".6"/><stop offset="1" stop-color="#34507a" stop-opacity=".6"/></linearGradient></defs>
  <path d="M0 372H850C1060 360 1190 250 1200 90V847H0Z" fill="#fff"/>
  <path d="M0 384H850C1060 374 1195 260 1200 100V847H0Z" fill="#0f53a8"/>
</svg>
<h2 class="abs cta-title">What are you still<br>looking for?</h2>
<a class="btn" style="left:506px;top:3220px;width:188px;height:63px">Contact us now</a>

<h3 class="abs footer-title" style="left:79px">Get In Touch</h3>
<div class="contact-row footer-text" style="top:3510px">
  <svg viewBox="0 0 22 22" fill="#fff"><path d="M11 1a7 7 0 00-7 7c0 5 7 13 7 13s7-8 7-13a7 7 0 00-7-7zm0 10a3 3 0 110-6 3 3 0 010 6z"/></svg>
  <span>123, Address, State Name<br>City, Street, Zipcode</span>
</div>
<div class="contact-row footer-text" style="top:3573px">
  <svg viewBox="0 0 22 22" fill="#fff"><path d="M5 2l4 4-2 3c1 3 3 5 6 6l3-2 4 4-3 3C9 20 2 13 2 5z"/></svg>
  <span>123.456.7890</span>
</div>
<div class="contact-row footer-text" style="top:3612px">
  <svg viewBox="0 0 22 22" fill="none" stroke="#fff" stroke-width="1.6"><rect x="1" y="4" width="20" height="14"/><path d="M1 4l10 8 10-8M1 18l7-7M21 18l-7-7"/></svg>
  <span>info@pawrank.com</span>
</div>

<h3 class="abs footer-title" style="left:348px">Navigation</h3>
<ul class="abs foot-nav">
  <li class="current">Home</li><li>About</li><li>Services</li><li>Testimonial</li><li>Blog</li><li>Contact</li>
</ul>

<h3 class="abs footer-title" style="left:575px">Blog Post</h3>
<div class="post footer-text" style="top:3508px">
  <div class="post-thumb" role="img" aria-label="Blog photo of a smiling woman" style="background:linear-gradient(150deg,#e8d7c6,#a78a6e)"></div>
  <div style="font-size:13.5px">Lorem Ipsum is simply<br>dummy text of the.<small>20 July 2019</small></div>
</div>
<div class="post footer-text" style="top:3607px">
  <div class="post-thumb" role="img" aria-label="Blog photo of a team at work" style="background:linear-gradient(150deg,#d2dde9,#5d7391)"></div>
  <div style="font-size:13.5px">Lorem Ipsum is simply<br>dummy text of the.<small>20 July 2019</small></div>
</div>

<h3 class="abs footer-title" style="left:885px">Newsletter</h3>
<p class="abs footer-text" style="left:885px;top:3510px;font-size:13.5px">To receive email releases, simply<br>provide us with your email below</p>
<div class="abs email-field">
  <svg width="20" height="16" viewBox="0 0 20 16" fill="#666"><path d="M0 0h20v16H0zM2 2l8 6 8-6z" fill-rule="evenodd"/></svg>
  <span>Email</span>
</div>
<a class="btn subscribe">Subscribe now</a>

<div class="abs footer-line"></div>
<p class="abs copyright">© Copyright - <b>PawRank</b> - 2019. All Right Reserved</p>

</body>
</html>
```